The most modern business card ever !!!

Our company call “Vantilo”. Vantilo is a technology company specialized in cruises solutions. Out main product is a platform to reserve cruises. This is a revolutionary platform that make easier to travel agencies and final users to reserve cruises across dozen companies like tarvik, welbi, dpv, hbt, etc..We are a “start up”, with a young team of developers and we want to transmit it.. For it, we want something different, a modern business card that represent cruises and technology.. When someone receive this card, this person should say: wowww this is different… this is modern… this is a cruise related company..
Contact Information for Business Card
Requirements
Must have
- diferent, modern
Should not have
- traditions business card

```html
<!DOCTYPE html>
<html lang="en">
<head>
<meta charset="UTF-8">
<title>Vantilo Business Card</title>
<link rel="stylesheet" href="https://fonts.googleapis.com/css2?family=Roboto:wght@400;500;700&display=swap">
<style>
  :root {
    --page-bg: #d8d3d1;
    --card-bg: #7a6764;
    --accent: #26a6da;
    --accent-deep: #0b8db0;
    --text-light: #ffffff;
  }
  * { margin: 0; padding: 0; box-sizing: border-box; }
  html, body {
    width: 1200px;
    height: 1200px;
    overflow: hidden;
    background: var(--page-bg);
  }
  .card {
    position: absolute;
    left: 298px;
    top: 99px;
    width: 603px;
    height: 1002px;
    background: var(--card-bg);
    font-family: "Roboto", Arial, sans-serif;
    color: var(--text-light);
    box-shadow: 0 10px 30px rgba(0,0,0,0.18);
  }
  .brand-bar {
    position: absolute;
    left: 450px;
    top: 67px;
    width: 84px;
    height: 437px;
    background: linear-gradient(180deg, var(--accent-deep) 0%, var(--accent) 50%, var(--accent-deep) 100%);
  }
  .vertical {
    position: absolute;
    writing-mode: vertical-rl;
    transform: rotate(180deg);
    white-space: nowrap;
  }
  .brand-name {
    left: 336px;
    bottom: 498px;
    font-size: 104px;
    font-weight: 500;
    line-height: 1;
    letter-spacing: 3px;
    color: var(--text-light);
  }
  .identity {
    left: 70px;
    bottom: 598px;
    font-size: 29px;
    line-height: 38px;
    letter-spacing: 4px;
  }
  .identity .person-name { color: var(--accent); font-weight: 500; }
  .identity .designation { color: var(--text-light); font-weight: 400; letter-spacing: 3px; }
  .marker {
    position: absolute;
    left: 68px;
    width: 82px;
    height: 19px;
  }
  .marker--accent { top: 462px; background: var(--accent); }
  .marker--light { top: 485px; background: var(--text-light); }
  .contact-list {
    position: absolute;
    left: 67px;
    top: 713px;
    list-style: none;
    font-size: 28px;
    letter-spacing: 1.6px;
    line-height: 58px;
  }
  .web-link {
    position: absolute;
    left: 67px;
    top: 895px;
    width: 470px;
    height: 44px;
  }
  .web-link svg { position: absolute; inset: 0; }
  .web-link span {
    position: relative;
    display: block;
    text-align: center;
    line-height: 44px;
    font-size: 27px;
    letter-spacing: 1.4px;
  }
  .web-link b { font-weight: 700; }
</style>
</head>
<body>
  <div class="card">
    <div class="brand-bar"></div>
    <div class="vertical brand-name">Vantilo</div>
    <div class="vertical identity">
      <div class="person-name">Your Name Here</div>
      <div class="designation">Designation</div>
    </div>
    <div class="marker marker--accent"></div>
    <div class="marker marker--light"></div>
    <ul class="contact-list">
      <li>- Contact@vantilo.io</li>
      <li>- 123 +4567 8910 111</li>
      <li>- Main Avenue Street 123. Etc</li>
    </ul>
    <div class="web-link">
      <svg width="470" height="44" viewBox="0 0 470 44">
        <path d="M24 0 H470 L458 26 Q450 44 430 44 H0 L7 18 Q12 0 24 0 Z" fill="var(--accent-deep)"/>
      </svg>
      <span>www.<b>YourSite</b>.com</span>
    </div>
  </div>
</body>
</html>
```